Web Design for an Online Dating Web Site

We need an uncoded web design for a new online dating web site called zMatchy.net. Simplicity and boldness are the key factors in the successful design.
Please look at the requirements document attached for details.
Updates
Dear all,
Please AVOID USING A PICTURE OF A HAPPY COUPLE ON THE HOME PAGE of the site. We highly want to move away from this space as it makes our web site just like another dating web site.
We like something simple with web 2.0 look and feel. The examples in the Requirements Document are exactly the design we are after.
Regards
Tarn
Industry/Entity Type
Dating
Look and feel
Each slider illustrates characteristics of the customer's brand and the style your logo design should communicate.

```html
<!DOCTYPE html>
<html lang="en">
<head>
<meta charset="utf-8">
<title>zMatchy.net</title>
<link href="https://fonts.googleapis.com/css2?family=Arimo:wght@400;700&family=Varela+Round&display=swap" rel="stylesheet">
<style>
:root{
  --pink:#e6197f;
  --pink-light:#f25aa6;
  --orange:#f7a21b;
  --green:#5f8a12;
  --green-dark:#3f5f0a;
  --bg-top:#2b2b2b;
  --bg-dark:#161616;
  --bg-mid:#222;
  --panel:#1c1c1c;
  --line:#3a3a3a;
  --text:#cfcfcf;
  --muted:#8a8a8a;
  --teal:#4fc3d9;
  --white:#fff;
}
*{box-sizing:border-box;margin:0;padding:0}
html,body{width:720px;height:1200px;overflow:hidden}
body{background:var(--bg-dark);font-family:"Arimo",Arial,sans-serif;color:var(--text);position:relative;font-size:9px}
.abs{position:absolute}

/* header */
.site-header{left:0;top:0;width:720px;height:176px;background:linear-gradient(#333,#1d1d1d)}
.brand{left:0;top:18px;width:720px;text-align:center}
.brand-name{font-size:46px;font-weight:700;color:var(--pink);letter-spacing:-1px;line-height:50px}
.brand-site{font-size:10px;color:var(--muted);margin-top:-2px;padding-left:120px}
.main-nav{left:198px;top:94px;width:324px;height:22px;display:flex;justify-content:space-between;align-items:center}
.main-nav a{color:var(--white);text-decoration:none;font-size:9px;font-weight:700;padding:5px 11px;border-radius:10px}
.main-nav a.active{background:linear-gradient(var(--pink-light),var(--pink))}
.login-bar{left:48px;top:130px;width:624px;height:34px}
.login-tag{left:0;top:0;background:var(--pink);color:var(--white);font-size:9px;font-weight:700;padding:3px 8px;border-radius:2px}
.login-field{top:18px;height:14px;width:130px;background:#111;border:1px solid #444;border-radius:2px;color:#555;font-size:8px;padding:1px 5px}
.login-btn{left:278px;top:17px;width:56px;height:16px;background:linear-gradient(var(--orange),#d9820a);border-radius:8px;color:var(--white);font-size:8px;font-weight:700;text-align:center;line-height:16px}
.social{left:348px;top:14px;display:flex;gap:6px}
.social span{width:20px;height:20px;border-radius:3px;display:block}

/* hero */
.hero{left:0;top:176px;width:720px;height:264px;background:radial-gradient(ellipse 340px 150px at 50% 50%,#3a3a3a,#141414)}
.hero-title{left:0;top:40px;width:720px;text-align:center;font-family:"Varela Round",Arial,sans-serif;font-size:34px;color:var(--pink)}
.hero-title .accent{color:var(--orange)}
.hero-visual{left:108px;top:96px;width:196px;height:136px;border-radius:12px;background:linear-gradient(135deg,#f04040,#a80c0c)}
.hero-copy{left:324px;top:126px;width:208px;font-size:12px;line-height:15px;color:var(--white)}
.learn-more{left:552px;top:120px;width:106px;height:106px;border-radius:50%;background:radial-gradient(circle at 40% 35%,#7fae1f,var(--green-dark));border:3px solid #2a2a2a;text-align:center;color:var(--white);font-size:8px;padding-top:38px}
.learn-more b{display:block;font-size:12px;margin-top:3px}
.slide-arrow{top:138px;width:20px;height:32px;background:#bbb;display:flex;align-items:center;justify-content:center}

/* content */
.content{left:0;top:440px;width:720px;height:516px;background:var(--bg-mid)}
.col-title{font-size:11px;font-weight:700;color:var(--white);border-bottom:1px solid var(--line);padding-bottom:5px}
.recent{left:90px;top:26px;width:342px}
.post{position:relative;margin-top:14px}
.post-visual{height:150px;background:linear-gradient(#5a5a3a,#3d3d25);border:4px solid #333}
.post-date{position:absolute;left:8px;top:8px;width:34px;height:38px;background:#2d5f6f;color:var(--white);text-align:center;font-size:14px;font-weight:700;line-height:18px;padding-top:2px}
.post-date small{display:block;font-size:7px;line-height:8px}
.post-tag{position:absolute;right:8px;top:136px;font-size:7px;color:var(--white);display:flex;align-items:center;gap:3px}
.post h3{font-size:12px;color:var(--white);margin-top:8px}
.post p{font-size:7px;line-height:10px;color:var(--muted);margin-top:4px}
.read-more{display:inline-block;margin-top:6px;background:#444;color:var(--white);font-size:7px;padding:2px 7px;border-radius:6px}
.blog{left:468px;top:26px;width:168px}
.blog-item{display:flex;gap:8px;margin-top:14px;height:34px}
.blog-thumb{width:34px;height:34px;background:linear-gradient(#c48a7a,#7a4a44);border:2px solid #555;flex:none}
.blog-item b{display:block;color:var(--teal);font-size:8px}
.blog-item span{font-size:7px;color:var(--muted)}
.blog-item em{font-style:normal;background:#444;color:var(--white);font-size:6px;padding:1px 4px;border-radius:4px;margin-left:4px}
.video{left:468px;top:340px;width:168px;height:122px;background:linear-gradient(#7a5a40,#2a2018);border:3px solid #444}
.play{left:66px;top:42px}
.signup{left:486px;top:468px;width:130px;height:40px;border-radius:20px;background:linear-gradient(var(--pink-light),var(--pink));border:3px solid #555;color:var(--white);font-size:20px;font-family:"Varela Round",Arial,sans-serif;text-align:center;line-height:34px}

/* footer */
.site-footer{left:0;top:956px;width:720px;height:244px;background:#111;border-top:2px solid var(--line)}
.f-brand{left:88px;top:22px;font-size:24px;font-weight:700;color:var(--pink)}
.f-heading{font-size:11px;color:var(--pink);font-weight:700}
.f-links{left:88px;top:62px;width:110px}
.f-links li{list-style:none;font-size:7px;color:var(--muted);line-height:13px}
.tweets{left:258px;top:22px;width:170px}
.badges{position:absolute;left:0;top:22px;display:flex;flex-direction:column;gap:6px}
.badges span{width:32px;height:14px;background:#ddd;border-radius:2px;display:block}
.tweet{position:absolute;left:44px;width:128px;font-size:7px;line-height:10px;color:var(--muted)}
.tweet b{color:var(--teal);font-weight:400}
.contact{left:468px;top:22px;width:170px}
.contact .field{height:16px;background:#222;border:1px solid #444;margin-top:8px;font-size:7px;color:#666;padding:3px 5px}
.contact .field.tall{height:48px}
.submit{margin-top:8px;float:right;background:#444;color:var(--white);font-size:7px;padding:3px 8px;border-radius:6px}
.f-bottom{left:88px;top:222px;width:548px;font-size:7px;color:#666;display:flex;justify-content:space-between}
</style>
</head>
<body>
<header class="site-header abs">
  <div class="brand abs"><div class="brand-name">zmatchy</div><div class="brand-site">zMatchy.net</div></div>
  <nav class="main-nav abs">
    <a class="active">WHY ZMATCHY</a><a>HOW IT WORKS</a><a>SIGN UP</a><a>OUR BLOG</a>
  </nav>
  <div class="login-bar abs">
    <span class="login-tag abs">LOGIN</span>
    <span class="login-field abs" style="left:0">Username</span>
    <span class="login-field abs" style="left:138px">Password</span>
    <span class="login-btn abs">Log in</span>
    <div class="social abs">
      <span style="background:#3b5998"></span><span style="background:#2aa9e0"></span><span style="background:#e2e2e2"></span><span style="background:#7a4ec2"></span><span style="background:#2e6fb5"></span><span style="background:#d8d8d8"></span><span style="background:#f28a1e"></span>
    </div>
  </div>
</header>

<section class="hero abs">
  <h1 class="hero-title abs">Some <span class="accent">Slogn</span> Goes Here</h1>
  <div class="hero-visual abs" role="img" aria-label="Red glossy box with a white heart"></div>
  <p class="hero-copy abs">Lorem ipsum dolor sit amet, consectetur adipisicing elit, sed do eiusmod tempor incididunt ut labore et dolore magna aliqua.</p>
  <div class="learn-more abs">Click here to<b>LEARN MORE</b></div>
  <div class="slide-arrow abs" style="left:0"><svg width="8" height="10"><path d="M7 0L0 5L7 10Z" fill="#333"/></svg></div>
  <div class="slide-arrow abs" style="right:0"><svg width="8" height="10"><path d="M1 0L8 5L1 10Z" fill="#333"/></svg></div>
</section>

<main class="content abs">
  <section class="recent abs">
    <h2 class="col-title">RECENT POSTS</h2>
    <article class="post">
      <div class="post-visual" role="img" aria-label="Drawing of a couple holding hands"></div>
      <div class="post-date">12<small>OCT 2011</small></div>
      <span class="post-tag"><svg width="9" height="8"><path d="M4.5 8L0 3.5A2 2 0 0 1 4.5 1A2 2 0 0 1 9 3.5Z" fill="#e6197f"/></svg>Comments</span>
      <h3>Lorem ipsum dolor sit amet.</h3>
      <p>Lorem ipsum dolor sit amet, consectetur adipiscing elit, sed do eiusmod tempor incididunt ut labore et dolore magna aliqua. Ut enim ad minim veniam, quis nostrud exercitation ullamco laboris nisi ut aliquip ex ea commodo consequat.</p>
      <span class="read-more">Read More</span>
    </article>
    <article class="post">
      <div class="post-visual" role="img" aria-label="Drawing of a couple holding hands"></div>
      <div class="post-date">12<small>OCT 2011</small></div>
      <span class="post-tag"><svg width="9" height="8"><path d="M4.5 8L0 3.5A2 2 0 0 1 4.5 1A2 2 0 0 1 9 3.5Z" fill="#e6197f"/></svg>Comments</span>
      <h3>Lorem ipsum dolor sit amet.</h3>
      <p>Lorem ipsum dolor sit amet, consectetur adipiscing elit, sed do eiusmod tempor incididunt ut labore et dolore magna aliqua. Ut enim ad minim veniam, quis nostrud exercitation ullamco laboris nisi ut aliquip ex ea commodo consequat.</p>
      <span class="read-more">Read More</span>
    </article>
  </section>

  <aside class="blog abs">
    <h2 class="col-title">LATEST BLOG POSTS</h2>
    <div class="blog-item"><div class="blog-thumb" role="img" aria-label="Couple photo"></div><div><b>Lorem ipsum dolor sit amet.</b><span>Jan 01, 2011 | 2 comments</span><em>More</em></div></div>
    <div class="blog-item"><div class="blog-thumb" role="img" aria-label="Couple photo"></div><div><b>Lorem ipsum dolor sit amet.</b><span>Jan 01, 2011 | 2 comments</span><em>More</em></div></div>
    <div class="blog-item"><div class="blog-thumb" role="img" aria-label="Couple photo"></div><div><b>Lorem ipsum dolor sit amet.</b><span>Jan 01, 2011 | 2 comments</span><em>More</em></div></div>
    <div class="blog-item"><div class="blog-thumb" role="img" aria-label="Couple photo"></div><div><b>Lorem ipsum dolor sit amet.</b><span>Jan 01, 2011 | 2 comments</span><em>More</em></div></div>
    <div class="blog-item"><div class="blog-thumb" role="img" aria-label="Couple photo"></div><div><b>Lorem ipsum dolor sit amet.</b><span>Jan 01, 2011 | 2 comments</span><em>More</em></div></div>
  </aside>
  <div class="video abs" role="img" aria-label="Video still of a couple">
    <svg class="play abs" width="34" height="34"><circle cx="17" cy="17" r="16" fill="#6cbf2a" stroke="#fff" stroke-width="2"/><path d="M13 10L24 17L13 24Z" fill="#fff"/></svg>
  </div>
  <div class="signup abs">Sign Up</div>
</main>

<footer class="site-footer abs">
  <div class="f-brand abs">zmatchy</div>
  <div class="f-links abs">
    <h3 class="f-heading">Read More</h3>
    <ul><li>Why zMatchy</li><li>How It Works</li><li>Sign Up</li><li>Our Blog</li><li>Contact Us</li><li>Privacy</li></ul>
  </div>
  <div class="tweets abs">
    <h3 class="f-heading" style="padding-left:44px">Latest Tweets</h3>
    <div class="badges"><span></span><span></span><span></span><span></span><span></span><span></span><span></span><span></span></div>
    <p class="tweet" style="top:24px"><b>@zmatchy</b> Lorem ipsum dolor sit amet, consectetur adipiscing elit sed do.</p>
    <p class="tweet" style="top:74px"><b>@zmatchy</b> Lorem ipsum dolor sit amet, consectetur adipiscing elit sed do.</p>
    <p class="tweet" style="top:124px"><b>@zmatchy</b> Lorem ipsum dolor sit amet, consectetur adipiscing elit sed do.</p>
  </div>
  <div class="contact abs">
    <h3 class="f-heading">Let's Talk</h3>
    <div class="field">Name</div><div class="field">Email</div><div class="field tall">Comment</div>
    <span class="submit">Submit</span>
  </div>
  <div class="f-bottom abs"><span>Copyright © 2011 zMatchy</span><span>Privacy Policy &nbsp; Terms &amp; Conditions</span></div>
</footer>
</body>
</html>
```